ORVANE EV

We need a business card design for a new Luxury golf cart Company Orvane. We manufacture and sell high end golf carts. We would like to see designs that are high end. I have the logo so really need a nice clean look.

```html
<!DOCTYPE html>
<html lang="en">
<head>
<meta charset="utf-8">
<title>Orvane EV – Business Card</title>
<link href="https://fonts.googleapis.com/css2?family=Open+Sans:wght@400;600;800&display=swap" rel="stylesheet">
<style>
  :root {
    --backdrop: #3b3b3b;
    --card: #0f0f0f;
    --card-edge: #1f8f7f;
    --teal: #1f9e8a;
    --silver: #d4d6d8;
    --text: #e9e9e9;
    --pattern-dark: #121212;
    --pattern-light: #1c1c1c;
  }
  * { margin: 0; padding: 0; box-sizing: border-box; }
  html, body { width: 1200px; height: 801px; overflow: hidden; }
  body {
    background: var(--backdrop);
    font-family: "Open Sans", Arial, sans-serif;
    position: relative;
  }
  .card {
    position: absolute;
    top: 246px;
    width: 540px;
    height: 309px;
    background: var(--card);
    border-bottom: 2px solid var(--card-edge);
    border-right: 1px solid var(--card-edge);
    overflow: hidden;
  }
  .card--front { left: 40px; }
  .card--back { left: 620px; }

  .brand {
    position: absolute;
    left: 44px;
    top: 100px;
    width: 264px;
    text-align: center;
    font-weight: 800;
    font-size: 46px;
    letter-spacing: 3px;
    color: var(--silver);
    line-height: 1;
    white-space: nowrap;
  }
  .person {
    position: absolute;
    left: 96px;
    top: 186px;
    width: 220px;
    text-align: right;
  }
  .person__name {
    color: var(--teal);
    font-weight: 600;
    font-size: 19px;
    letter-spacing: 0.5px;
    white-space: nowrap;
  }
  .person__role {
    color: var(--text);
    font-size: 13px;
    margin-top: 2px;
  }
  .divider {
    position: absolute;
    left: 334px;
    top: 112px;
    width: 1px;
    height: 84px;
    background: var(--teal);
  }
  .contact {
    position: absolute;
    left: 354px;
    top: 118px;
    list-style: none;
  }
  .contact li {
    display: flex;
    align-items: center;
    gap: 8px;
    color: var(--text);
    font-size: 13px;
    line-height: 24px;
    white-space: nowrap;
  }
  .contact svg { width: 11px; height: 11px; flex: none; }
  .icon-fill { fill: var(--teal); }
  .icon-line { fill: none; stroke: var(--teal); stroke-width: 2.5; }

  .pattern {
    position: absolute;
    inset: 0;
    background: linear-gradient(135deg, var(--pattern-light), var(--pattern-dark) 60%);
  }
  .back-mark {
    position: absolute;
    left: 300px;
    top: 196px;
    padding: 5px 12px;
    border: 1px solid var(--silver);
    border-radius: 4px;
    background: var(--card);
    font-weight: 800;
    font-size: 18px;
    letter-spacing: 1.5px;
    color: var(--silver);
    line-height: 1.2;
  }
</style>
</head>
<body>
  <section class="card card--front">
    <div class="brand">ORVANE</div>
    <div class="person">
      <p class="person__name">DANIEL HARROW</p>
      <p class="person__role">President</p>
    </div>
    <div class="divider"></div>
    <ul class="contact">
      <li>
        <svg viewBox="0 0 24 24" aria-hidden="true"><path class="icon-fill" d="M6.6 10.8a15 15 0 0 0 6.6 6.6l2.2-2.2a1 1 0 0 1 1-.25 11.4 11.4 0 0 0 3.6.57 1 1 0 0 1 1 1V20a1 1 0 0 1-1 1A17 17 0 0 1 3 4a1 1 0 0 1 1-1h3.5a1 1 0 0 1 1 1c0 1.25.2 2.45.57 3.57a1 1 0 0 1-.25 1z"/></svg>
        555-014-2270
      </li>
      <li>
        <svg viewBox="0 0 24 24" aria-hidden="true"><rect class="icon-line" x="2" y="5" width="20" height="14"/><path class="icon-line" d="M2 5l10 8 10-8"/></svg>
        d.harrow@orvane.com
      </li>
      <li>
        <svg viewBox="0 0 24 24" aria-hidden="true"><circle class="icon-line" cx="12" cy="12" r="10"/><path class="icon-line" d="M2 12h20M12 2c4 4 4 16 0 20M12 2c-4 4-4 16 0 20"/></svg>
        www.Orvane.com
      </li>
    </ul>
  </section>

  <section class="card card--back">
    <div class="pattern" role="img" aria-label="Tone-on-tone repeating brand pattern in dark gloss on black"></div>
    <div class="back-mark">ORVANE</div>
  </section>
</body>
</html>
```